1.ターゲット層は30〜60代の投資家ですが、60代が多めです。

2.グローバルナビ含め、トップページ内のコンテンツは同じですが、各コンテンツの掲載箇所等にこだわりはありませんので自由にデザインして下さい。

3.コンテンツエリアは、2カラム(メイン・右ナビ)で
それぞれのサイズは下記になります。
・メイン:650px
・右ナビ:300px
(メインと右ナビの間が10px)

4.できるだけ幅広いデザインを頂きたいため、
デザインのイメージ等はこちらから指示致しません。
※ご不明点はご質問ください。

5.なおトップロゴは現行のものを利用しますのでデザインの必要ありません。
広告箇所も同じくデザインの必要はありません。
※デザインの必要が無い箇所は添付赤枠部分となります。
※広告はデザインに合わせて配置いたしますので広告箇所をご指定頂く必要はありませ

ご不明な点がありましたら、お気軽にご連絡ください。
http://tsukimado.jp/
3ページ
• イラストレーター形式 (.ai)
• フォトショップ形式 (.psd)
基本のフォントサイズも特に指定ございません。

当選者については、アイコンなどになる部分に関して、決定後、切り出しやすいように定義していただきます。

【契約上のご注意】
・採用対象となる方には当社フォーマットの契約書を締結させて頂きます。
※添付「クラウドソーシング向け業務委託契約書_提示締結用.pdf」
【10月21日追記】
提案数が1件しか集まっていないため、募集期間を1週間延長させました。

新期限:10/28

既にご提案頂いた方、当初の期限までにご提案頂く予定だった方は大変申し訳ございません。
もう暫くお待ち下さい。
たくさんのご提案をいただきありがとうございます。
お礼ご返信も間に合っておりませんが、ご返信していないご提案も
全て検討対象とさせて頂きますのでご安心ください。

今後のスケジュールに関しまして追記させて頂きます。
ご提案頂いたデザインを当社上層部に提出し社内検討をさせて頂きます。

上層部スケジュールを合わせて会議を実施・決定の流れになりますので、
日程調整等でもう暫くお時間を頂戴できればと存じます。

色合いや全体イメージを社内複数人による多数決により決定させていただきました。

たくさんのご応募ありがとうございました。
本件につきましては社内調整等、
選定まで時間がかかりましたことお詫びいたします。

また本コンペは3件の当選予定をしておりまして、
今回決定の1件以外に別途2名の方に個別にプロジェクト形式でご発注させていただいております。

```html
<!DOCTYPE html>
<html lang="ja">
<head>
<meta charset="utf-8">
<title>Tsukimado 株式情報</title>
<link rel="stylesheet" href="https://fonts.googleapis.com/css2?family=Noto+Sans+JP:wght@400;700&display=swap">
<style>
:root{
  --navy:#1b3a68;
  --nav:#2b5a98;
  --nav-dark:#16335e;
  --sky:#e9f1fb;
  --sky-line:#c9d9ee;
  --orange:#e8731c;
  --red:#d9332b;
  --green:#3a9d4f;
  --gold:#f3c531;
  --text:#333;
  --muted:#777;
  --line:#d6dbe3;
  --bg:#f2f4f7;
  --white:#fff;
}
*{box-sizing:border-box;margin:0;padding:0}
html,body{width:1200px;height:2860px;overflow:hidden}
body{font-family:"Noto Sans JP",sans-serif;font-size:12px;color:var(--text);background:var(--bg);position:relative}
a{color:inherit;text-decoration:none}

/* header */
.header{height:72px;background:var(--white);display:flex;align-items:center;padding:0 60px;gap:30px}
.brand{display:flex;align-items:center;gap:8px;font-size:26px;font-weight:700;color:var(--navy);width:240px}
.brand-dot{width:14px;height:14px;background:var(--orange);border-radius:50%}
.indices{display:flex;flex:1;gap:14px}
.index{flex:1;border-left:1px solid var(--line);padding-left:12px}
.index-name{font-size:10px;color:var(--muted)}
.index-val{font-size:20px;font-weight:700;color:var(--navy)}
.index-chg{font-size:10px;color:var(--red)}
.nav{height:32px;background:var(--nav);display:flex;padding:0 60px}
.nav a{color:var(--white);font-size:12px;font-weight:700;padding:0 22px;line-height:32px;border-right:1px solid var(--nav-dark)}
.nav a.on{background:var(--gold);color:var(--navy)}
.search{height:32px;background:var(--sky);border-bottom:1px solid var(--sky-line);display:flex;align-items:center;padding:0 60px;gap:10px}
.search-box{width:520px;height:22px;background:var(--white);border:1px solid var(--sky-line);font-size:10px;color:var(--muted);padding:3px 8px}
.search-btn{height:22px;width:60px;background:var(--navy);color:var(--white);font-size:11px;text-align:center;line-height:22px}
.search-note{margin-left:auto;font-size:10px;color:var(--muted)}

/* layout */
.content{position:absolute;top:144px;left:60px;width:1080px;display:flex;gap:14px}
.main{width:730px;display:flex;flex-direction:column;gap:10px}
.side{width:336px;display:flex;flex-direction:column;gap:10px}
.box{background:var(--white);border:1px solid var(--line)}
.box-head{height:28px;background:var(--navy);color:var(--white);font-weight:700;font-size:13px;padding:0 10px;display:flex;align-items:center;justify-content:space-between}
.box-head small{font-weight:400;font-size:10px;color:#cdd8ea}
.box-head.light{background:var(--sky);color:var(--navy);border-bottom:2px solid var(--nav)}
.box-head.light small{color:var(--muted)}
.more{font-size:10px;color:var(--nav);text-align:right;padding:6px 10px;line-height:14px}
.placeholder{background:linear-gradient(135deg,#dfe6ef,#c7d3e3)}
.tag{display:inline-block;font-size:9px;line-height:14px;color:var(--white);background:var(--orange);padding:1px 5px;margin-right:6px;vertical-align:middle}
.tag.blue{background:var(--nav)}
.tag.red{background:var(--red)}

/* top news */
.topnews{height:256px;display:flex}
.topnews-charts{width:200px;padding:10px;display:flex;flex-direction:column;gap:8px;border-right:1px solid var(--line)}
.mini-chart{height:100px;border:1px solid var(--line);background:var(--white)}
.topnews-list{flex:1;padding:6px 12px}
.topnews-list li{list-style:none;font-size:11px;line-height:26px;height:27px;border-bottom:1px dotted var(--line);white-space:nowrap;overflow:hidden}
.topnews-menu{width:150px;padding:8px;display:flex;flex-direction:column;gap:6px;background:var(--sky)}
.topnews-menu a{background:var(--white);border:1px solid var(--sky-line);font-size:11px;font-weight:700;color:var(--navy);padding:5px 6px;display:flex;align-items:center}
.topnews-menu a::before{content:"";width:14px;height:14px;background:var(--orange);margin-right:6px}

.linkrow{height:32px;display:flex;align-items:center;gap:30px;padding:0 14px;font-size:11px;color:var(--nav);background:var(--white);border:1px solid var(--line)}
.ad-wide{height:52px}

/* earnings */
.earnings-body{display:flex;padding:8px 10px;gap:10px}
.earnings-list{flex:1}
.earn-item{display:flex;gap:8px;padding:6px 0;border-bottom:1px dotted var(--line)}
.earn-date{width:70px;font-size:10px;color:var(--muted);line-height:17px}
.earn-text{flex:1;font-size:11px;line-height:17px}
.earnings-chart{width:190px;height:200px;border:1px solid var(--line)}

.promo{height:52px;background:var(--nav);color:var(--white);padding:8px 14px;font-size:11px;line-height:18px}
.promo b{color:var(--gold)}

/* ranking table */
.tabs{display:flex;gap:2px;padding:6px 10px 0}
.tabs span{font-size:10px;padding:3px 10px;background:var(--sky);color:var(--navy)}
.tabs span.on{background:var(--orange);color:var(--white)}
table{width:100%;border-collapse:collapse;font-size:11px}
.rank-table{width:calc(100% - 20px);margin:6px 10px 10px}
.rank-table th{background:var(--sky);color:var(--navy);font-weight:700;padding:4px;border:1px solid var(--sky-line);font-size:10px}
.rank-table td{padding:4px;border:1px solid var(--line);text-align:center}
.up{color:var(--red)}
.related-links{display:flex;gap:40px;padding:12px 14px;font-size:11px;color:var(--nav)}

/* news lists */
.newslist li{list-style:none;font-size:11px;line-height:18px;padding:6px 10px;border-bottom:1px solid var(--white);background:var(--sky);white-space:nowrap;overflow:hidden}
.newslist li:nth-child(even){background:#f6f9fd}
.newslist .time{color:var(--muted);margin-right:8px;font-size:10px}
.twocol{display:flex;gap:10px}
.twocol .box{flex:1}
.ad-square{width:300px;height:290px;margin:10px auto 0}

/* side */
.side-ad{height:156px}
.morning{height:60px;display:flex;align-items:center;gap:10px;padding:0 12px}
.morning-badge{background:var(--red);color:var(--white);font-weight:700;font-size:14px;padding:6px 10px}
.morning-text{font-size:16px;font-weight:700;color:var(--navy)}
.side-chart{height:100px}
.market-table td{padding:5px 10px;border-bottom:1px solid var(--line)}
.market-table td:nth-child(2){text-align:right;font-weight:700}
.market-table td:nth-child(3){text-align:right;width:60px}
.quiz{height:230px;text-align:center;padding:14px}
.quiz-title{font-size:16px;font-weight:700;color:var(--navy);margin-bottom:18px}
.quiz-buttons{display:flex;justify-content:center;gap:24px}
.quiz-btn{width:110px;height:110px;border-radius:50%;color:var(--white);font-size:24px;font-weight:700;display:flex;align-items:center;justify-content:center}
.quiz-btn.yes{background:var(--green)}
.quiz-btn.no{background:var(--red)}
.quiz-note{font-size:10px;color:var(--muted);margin-top:14px}
.side-links{height:100px;padding:8px 10px}
.side-links li{list-style:none;font-size:11px;line-height:22px;border-bottom:1px dotted var(--line)}

/* footer */
.footer{position:absolute;left:0;top:2640px;width:1200px;height:220px;background:var(--navy);color:#cdd8ea}
.footer-nav{display:flex;gap:34px;padding:22px 60px 14px;font-size:11px;border-bottom:1px solid #2e5186}
.footer-body{display:flex;justify-content:space-between;padding:18px 60px;font-size:10px;line-height:18px}
.footer-brand{display:flex;align-items:center;gap:8px;font-size:24px;font-weight:700;color:var(--white)}
.footer-url{font-size:10px;color:#cdd8ea;margin-top:4px;text-align:right}
</style>
</head>
<body>

<header class="header">
  <div class="brand"><span class="brand-dot"></span>Tsukimado</div>
  <div class="indices">
    <div class="index"><div class="index-name">日経平均</div><div class="index-val">15,001.97</div><div class="index-chg">+81.72 (+0.55%)</div></div>
    <div class="index"><div class="index-name">ドル/円</div><div class="index-val">108.65</div><div class="index-chg">+0.21 (+0.19%)</div></div>
    <div class="index"><div class="index-name">マザーズ</div><div class="index-val">2,198.34</div><div class="index-chg">+12.05 (+0.55%)</div></div>
    <div class="index"><div class="index-name">ジャスダック</div><div class="index-val">862.55</div><div class="index-chg">+3.40 (+0.40%)</div></div>
  </div>
</header>
<nav class="nav">
  <a class="on">トップ</a><a>市場ニュース</a><a>決算速報</a><a>株価注意報</a><a>企業情報</a><a>特集</a><a>ランキング</a><a>チャート</a><a>マイページ</a>
</nav>
<div class="search">
  <div class="search-box">銘柄コード・銘柄名を入力してください</div>
  <div class="search-btn">検索</div>
  <div class="search-note">http://tsukimado.jp/ ｜ ログイン ｜ 会員登録</div>
</div>

<div class="content">
  <main class="main">

    <section class="box topnews">
      <div class="topnews-charts">
        <svg class="mini-chart" viewBox="0 0 180 100"><text x="6" y="12" font-size="9" fill="#1b3a68">日経平均</text><polyline fill="none" stroke="#2b5a98" stroke-width="1.5" points="6,80 25,70 40,74 58,55 75,60 92,45 110,50 128,35 146,40 170,22"/><line x1="6" y1="90" x2="174" y2="90" stroke="#d6dbe3"/></svg>
        <svg class="mini-chart" viewBox="0 0 180 100"><text x="6" y="12" font-size="9" fill="#1b3a68">NYダウ</text><polyline fill="none" stroke="#d9332b" stroke-width="1.5" points="6,40 25,48 40,42 58,60 75,55 92,68 110,62 128,72 146,66 170,78"/><line x1="6" y1="90" x2="174" y2="90" stroke="#d6dbe3"/></svg>
      </div>
      <ul class="topnews-list">
        <li><span class="tag">注目</span>東証大引け 日経平均は続伸、主力株に買い戻し</li>
        <li><span class="tag">注目</span>来週の相場見通し 円安基調で輸出株に期待感</li>
        <li><span class="tag blue">決算</span>電子部品大手、通期利益予想を上方修正</li>
        <li><span class="tag blue">決算</span>小売大手の上期営業益は前年比二割増に</li>
        <li><span class="tag">注目</span>新興市場は小幅高、材料株に個人の資金流入</li>
        <li><span class="tag red">速報</span>米雇用統計を控え、様子見ムード強まる</li>
        <li><span class="tag">注目</span>海運株が軒並み高、運賃指数の上昇を好感</li>
        <li><span class="tag blue">決算</span>機械大手、受注回復で増配を発表</li>
        <li><span class="tag">注目</span>後場の寄り付き 買い優勢で推移</li>
      </ul>
      <div class="topnews-menu">
        <a>リアルタイム</a><a>株価注意報</a><a>決算速報</a><a>テーマ株</a><a>ランキング</a><a>IPO情報</a><a>株主優待</a>
      </div>
    </section>

    <div class="linkrow"><a>新着ニュース一覧</a><a>市況ニュース</a><a>材料ニュース</a><a>特集記事</a><a>コラム</a></div>

    <div class="placeholder ad-wide" role="img" aria-label="企業分析アプリの広告バナー（Kazeya）"></div>

    <section class="box earnings">
      <div class="box-head">決算速報 <small>更新 15:30</small></div>
      <div class="earnings-body">
        <div class="earnings-list">
          <div class="earn-item"><div class="earn-date">10/21 15:00</div><div class="earn-text"><span class="tag blue">上方</span>半導体装置メーカー、今期経常を二割上方修正</div></div>
          <div class="earn-item"><div class="earn-date">10/21 15:00</div><div class="earn-text"><span class="tag red">下方</span>化学メーカー、原料高で通期予想を引き下げ</div></div>
          <div class="earn-item"><div class="earn-date">10/21 14:30</div><div class="earn-text"><span class="tag blue">上方</span>食品大手、上期経常が計画を上回って着地</div></div>
          <div class="earn-item"><div class="earn-date">10/21 14:00</div><div class="earn-text"><span class="tag">増配</span>商社、年間配当を前期から五円増額へ</div></div>
          <div class="earn-item"><div class="earn-date">10/21 13:30</div><div class="earn-text"><span class="tag blue">上方</span>住宅設備メーカー、受注好調で利益予想を修正</div></div>
          <div class="earn-item"><div class="earn-date">10/21 13:00</div><div class="earn-text"><span class="tag red">下方</span>精密機器、海外需要の鈍化で減益見通し</div></div>
        </div>
        <svg class="earnings-chart" viewBox="0 0 190 200"><text x="8" y="16" font-size="10" fill="#1b3a68">上方修正 件数</text><rect x="20" y="120" width="22" height="60" fill="#2b5a98"/><rect x="55" y="90" width="22" height="90" fill="#2b5a98"/><rect x="90" y="100" width="22" height="80" fill="#2b5a98"/><rect x="125" y="60" width="22" height="120" fill="#e8731c"/><line x1="10" y1="180" x2="180" y2="180" stroke="#d6dbe3"/></svg>
      </div>
      <div class="more">決算速報一覧へ ›</div>
    </section>

    <div class="promo"><b>■ 特集</b> 今週の注目決算 半導体・電子部品・商社（10月28日まで）<br>来週の決算発表予定 ｜ 個別銘柄の業績推移をチェック（10/22）</div>

    <div class="placeholder ad-wide" role="img" aria-label="投資サービスの広告バナー"></div>

    <section class="box ranking">
      <div class="box-head light">注目銘柄 ランキング <small>10/21 15:00</small></div>
      <div class="tabs"><span class="on">値上がり率</span><span>値下がり率</span><span>出来高</span><span>売買代金</span></div>
      <table class="rank-table">
        <tr><th>順位</th><th>コード</th><th>市場</th><th>銘柄名</th><th>株価</th><th>前日比</th><th>騰落率</th></tr>
        <tr><td>1</td><td>0011</td><td>東1</td><td>ハルカゼ工業</td><td>92</td><td class="up">+11</td><td class="up">+13.58%</td></tr>
        <tr><td>2</td><td>0023</td><td>東1</td><td>ソラノ精機</td><td>588</td><td class="up">+62</td><td class="up">+11.79%</td></tr>
        <tr><td>3</td><td>0036</td><td>東M</td><td>アオミネ創薬</td><td>4,050</td><td class="up">+405</td><td class="up">+11.11%</td></tr>
        <tr><td>4</td><td>0048</td><td>JQ</td><td>ユキシロ電子</td><td>316</td><td class="up">+30</td><td class="up">+10.49%</td></tr>
        <tr><td>5</td><td>0052</td><td>東M</td><td>カスミ通商</td><td>1,820</td><td class="up">+160</td><td class="up">+9.64%</td></tr>
      </table>
    </section>

    <section class="box related">
      <div class="box-head light">関連ランキング</div>
      <div class="related-links"><a>› 株価急騰</a><a>› 年初来高値</a><a>› 出来高急増</a><a>› 新高値銘柄</a></div>
    </section>

    <section class="box majornews">
      <div class="box-head">主要ニュース <small>10/21 15:30</small></div>
      <ul class="newslist">
        <li><span class="time">15:30</span>【市況】日経平均は続伸 輸出関連が指数を押し上げ</li>
        <li><span class="time">15:20</span>【材料】電子部品株が高い 新製品の受注拡大を評価</li>
        <li><span class="time">15:10</span>【注目】来週の決算発表予定 主力企業が相次ぐ</li>
        <li><span class="time">14:55</span>【市況】新興市場は堅調 バイオ関連に物色の動き</li>
        <li><span class="time">14:40</span>【特集】高配当利回り銘柄 上位ランキングを公開</li>
        <li><span class="time">14:20</span>【材料】自社株買いの発表で値を伸ばす銘柄続く</li>
        <li><span class="time">14:00</span>【市況】後場は買い優勢 円安の進行を追い風に</li>
        <li><span class="time">13:45</span>【注目】海外投資家の買い越しが三週連続に</li>
        <li><span class="time">13:30</span>【材料】不動産株に見直し買い 金利低下を意識</li>
        <li><span class="time">13:10</span>【市況】アジア株は総じて高い 上海指数も反発</li>
      </ul>
      <div class="more">主要ニュース一覧へ ›</div>
    </section>

    <div class="twocol">
      <section class="box">
        <div class="box-head">注目テーマ</div>
        <ul class="newslist">
          <li>1 人工知能関連</li><li>2 再生可能エネルギー</li><li>3 半導体製造装置</li><li>4 インバウンド</li><li>5 電気自動車</li><li>6 ロボット</li><li>7 クラウド</li><li>8 バイオ医薬</li><li>9 防衛関連</li>
        </ul>
      </section>
      <section class="box">
        <div class="box-head">新着ニュース</div>
        <ul class="newslist">
          <li><span class="time">15:30</span>大引け概況 主力株に買い</li>
          <li><span class="time">15:25</span>上方修正銘柄が株価を押し上げ</li>
          <li><span class="time">15:18</span>新興市場の値上がり上位を確認</li>
          <li><span class="time">15:10</span>配当予想の増額が相次ぐ</li>
          <li><span class="time">15:02</span>円相場は小幅な円安で推移</li>
          <li><span class="time">14:55</span>機関投資家の売買動向まとめ</li>
          <li><span class="time">14:48</span>信用残の増減ランキング更新</li>
          <li><span class="time">14:40</span>テーマ株に物色の矛先向かう</li>
          <li><span class="time">14:32</span>海外市場の動向と今夜の指標</li>
        </ul>
      </section>
    </div>

    <section class="box feature">
      <div class="box-head">特集・コラム <small>10/21 15:30</small></div>
      <ul class="newslist">
        <li><span class="tag">特集</span>今期増益予想で割安な銘柄をスクリーニング</li>
        <li><span class="tag">特集</span>株主優待の人気ランキング 十月版を公開</li>
        <li><span class="tag blue">コラム</span>個人投資家のための決算書の読み方入門</li>
        <li><span class="tag">特集</span>長期保有に向く高配当銘柄の選び方</li>
        <li><span class="tag blue">コラム</span>相場の流れを読む チャート分析の基本</li>
        <li><span class="tag">特集</span>年末相場に向けた注目テーマ総点検</li>
        <li><span class="tag blue">コラム</span>新規上場銘柄 初値の傾向と注意点</li>
        <li><span class="tag">特集</span>業績好調な中小型株をピックアップ</li>
        <li><span class="tag blue">コラム</span>為替と株価の関係をやさしく解説</li>
      </ul>
      <div class="more">特集・コラム一覧へ ›</div>
    </section>

    <div class="placeholder ad-square" role="img" aria-label="タブレット端末の広告"></div>
  </main>

  <aside class="side">
    <div class="placeholder side-ad" role="img" aria-label="株式情報サービスの広告バナー"></div>
    <div class="box morning"><span class="morning-badge">朝刊</span><span class="morning-text">今朝の市況 準備中</span></div>
    <svg class="box side-chart" viewBox="0 0 336 100"><text x="8" y="14" font-size="10" fill="#1b3a68">日経平均 日中足</text><polyline fill="none" stroke="#2b5a98" stroke-width="1.5" points="10,70 40,66 70,58 100,62 130,50 160,52 190,40 220,44 250,34 280,30 320,24"/><line x1="10" y1="88" x2="326" y2="88" stroke="#d6dbe3"/></svg>
    <section class="box">
      <div class="box-head">市場指標</div>
      <table class="market-table">
        <tr><td>日経平均</td><td>14,864.56</td><td class="up">+81.72</td></tr>
        <tr><td>TOPIX</td><td>1,237.96</td><td class="up">+8.41</td></tr>
        <tr><td>東証2部</td><td>3,953.33</td><td class="up">+12.06</td></tr>
        <tr><td>JASDAQ</td><td>2,185.49</td><td class="up">+5.77</td></tr>
        <tr><td>マザーズ</td><td>860.75</td><td class="up">+3.40</td></tr>
        <tr><td>ドル/円</td><td>108.65</td><td class="up">+0.21</td></tr>
        <tr><td>ユーロ/円</td><td>137.24</td><td class="up">+0.35</td></tr>
      </table>
    </section>
    <section class="box quiz">
      <div class="quiz-title">株式投資で失敗しない</div>
      <div class="quiz-buttons"><div class="quiz-btn yes">YES</div><div class="quiz-btn no">NO</div></div>
      <div class="quiz-note">あなたの投資スタイルを診断します</div>
    </section>
    <section class="box side-links">
      <ul>
        <li>› 株価アラート設定</li>
        <li>› ポートフォリオ管理</li>
        <li>› よくある質問</li>
      </ul>
    </section>
  </aside>
</div>

<footer class="footer">
  <div class="footer-nav"><a>会社概要</a><a>利用規約</a><a>個人情報保護方針</a><a>免責事項</a><a>広告掲載</a><a>お問い合わせ</a><a>サイトマップ</a></div>
  <div class="footer-body">
    <div>当サイトに掲載されている情報は投資判断の参考となる情報の提供を目的としたものです。<br>投資の最終判断はご自身の責任でお願いいたします。<br>掲載情報の無断転載を禁じます。</div>
    <div><div class="footer-brand"><span class="brand-dot"></span>Tsukimado</div><div class="footer-url">http://tsukimado.jp/</div></div>
  </div>
</footer>

</body>
</html>
```